Flyer-Design für Ofenservice Firma
Zielgruppe
Die Firma hat als Kerngeschäft Wartung, Reinigung, Reparatur und Inbetriebnahme von Öfen und Kaminen aller Art. Der Fokus liegt dabei auf Pelletöfen. Die Firma versteht sich als zuverlässiger Dienstleister mit gutem Preisleistungsverhältnis. Zielgruppe sind hauptsächlich private Bewohner von Einfamilienhäusern in der ländlichen Gegend (Hessen)
Aufgabenstellung
Zur Bekanntmachung nach Neugründung soll ein Faltflyer gestaltet werden mit insgesamt 6 Bereichen. Die Informationen, welche auf den Flyer sollen, entnehmen Sie bitte dem Entwurf (flyer.pdf). Dieser stellt nur eine erste Idee dar und darf gerne nach Belieben verändert bzw. neu gestaltet werden. Die enthaltenen Informationen, sollten im Großen und Ganzen aber beibehalten werden. Schön wäre evtl. auch eine Hervorhebung der Preise, da wir Preisführer im Markt sind. Auch die Bilder unseres Teams sollen in den Flyer integriert sein. Auf Anfrage kann ich auch gerne weitere Kamin- und Ofenfotos zur Verfügung stellen, für welche ich die Nutzungsrechte habe. Falls Sie weitere Informationen benötigen oder Fragen haben, kommen Sie gerne auf mich zu. Die Bilder dürfen gerne etwas ausgeschnitten werden. Es geht in erster Linie darum, dass die Kunden erkennen, welche Art von Ofen sie zu Hause haben.

```html
<!DOCTYPE html>
<html lang="de">
<head>
<meta charset="utf-8">
<title>Faltflyer Ofenservice – Innenseite</title>
<link href="https://fonts.googleapis.com/css2?family=Open+Sans:wght@300;400;600;700;800&display=swap" rel="stylesheet">
<style>
  :root {
    --page-bg: #e4e4e4;
    --slate: #3e4e59;
    --slate-dark: #334049;
    --orange: #e07016;
    --orange-light: #f08a2c;
    --text-dark: #3a3f44;
    --text-grey: #8d9296;
    --title-grey: #5b6167;
    --panel-light: #f4f4f4;
    --panel-mid: #e2e3e4;
    --white: #ffffff;
    --rule-blue: #3d6f96;
  }
  * { box-sizing: border-box; margin: 0; padding: 0; }
  html, body {
    width: 1200px; height: 900px; overflow: hidden;
    background: var(--page-bg);
    font-family: "Open Sans", Arial, sans-serif;
  }
  .brochure {
    position: absolute; left: 45px; top: 58px;
    width: 1110px; height: 785px;
    display: flex;
    box-shadow: 0 12px 30px rgba(0,0,0,.18);
  }
  .panel { position: relative; width: 370px; height: 100%; overflow: hidden; }

  /* ---------- Panel: Pelletöfen ---------- */
  .panel--pellet { background: var(--slate); }
  .pellet__photo {
    position: absolute; left: 0; right: 0; bottom: 0; height: 46%;
    background: linear-gradient(160deg, #c9ccce 0%, #9fa6ab 35%, #5b6670 70%, #8e9aa3 100%);
  }
  .pellet__dark {
    position: absolute; inset: 0;
    background: linear-gradient(180deg, var(--slate) 0%, var(--slate-dark) 100%);
    clip-path: polygon(0 0, 100% 0, 100% 74%, 0 58%);
  }
  .pellet__content { position: absolute; left: 40px; right: 30px; top: 48px; color: var(--white); }
  .title-thin { font-weight: 300; font-size: 34px; line-height: 1.05; }
  .title-bold { font-weight: 800; font-size: 34px; line-height: 1.1; }
  .pellet__content .title-thin, .pellet__content .title-bold { color: var(--white); }
  .lead { font-weight: 700; font-size: 11.5px; margin: 22px 0 10px; }
  .service-list { list-style: none; font-size: 11px; line-height: 1.45; }
  .service-list li { position: relative; padding-left: 14px; margin-bottom: 7px; }
  .service-list li::before { content: "•"; position: absolute; left: 0; top: 0; }
  .price-box {
    position: absolute; left: 40px; bottom: 42px; width: 250px;
    background: rgba(255,255,255,.88); padding: 14px 16px;
    font-size: 11.5px; line-height: 1.55; color: var(--text-dark);
  }
  .price-box strong, .price-block strong, .price-group strong { font-weight: 700; }
  .price--contract { color: var(--orange); }

  /* ---------- Panel: Scheitholzöfen ---------- */
  .panel--wood { background: linear-gradient(90deg, var(--panel-mid) 0%, var(--panel-light) 35%, var(--white) 100%); }
  .wood__content { position: absolute; left: 40px; right: 30px; top: 50px; color: var(--text-dark); }
  .wood__content .title-thin { color: var(--text-grey); font-size: 31px; line-height: 1.02; }
  .wood__content .title-bold { color: var(--title-grey); font-size: 31px; line-height: 1.02; }
  .wood__photo {
    position: absolute; left: 40px; right: 26px; top: 480px; height: 150px;
    background: linear-gradient(120deg, #3b2d26 0%, #7a4b2e 30%, #d27a2c 48%, #f3f0ea 60%, #9b6a43 80%, #4a3a30 100%);
  }
  .price-block {
    position: absolute; left: 40px; bottom: 60px;
    border-left: 3px solid var(--rule-blue); padding-left: 14px;
    font-size: 11.5px; line-height: 1.55; color: var(--text-dark);
  }

  /* ---------- Panel: Kachelöfen ---------- */
  .panel--tile { background: linear-gradient(90deg, var(--panel-light) 0%, var(--white) 100%); }
  .tile__photo {
    position: absolute; left: 0; right: 0; top: 0; height: 300px;
    background: linear-gradient(135deg, #b9773a 0%, #e0a760 35%, #f2e4cf 60%, #c98444 85%, #8d5424 100%);
  }
  .tile__band { position: absolute; left: 0; top: 260px; width: 370px; height: 70px; }
  .tile__content { position: absolute; left: 40px; right: 30px; top: 345px; color: var(--text-dark); }
  .tile__content .title-thin { color: var(--orange); font-size: 34px; }
  .tile__content .title-bold { color: var(--orange); font-size: 34px; }
  .dot-list { list-style: none; font-size: 11px; line-height: 1.5; margin-top: 20px; }
  .dot-list li { position: relative; padding-left: 22px; margin-bottom: 12px; }
  .dot-list li::before {
    content: ""; position: absolute; left: 0; top: 4px;
    width: 8px; height: 8px; border-radius: 50%; background: var(--orange);
  }
  .price-group { font-size: 11.5px; line-height: 1.5; margin-top: 18px; }
</style>
</head>
<body>
<main class="brochure">

  <section class="panel panel--pellet">
    <div class="pellet__photo" role="img" aria-label="Foto: Wohnraum mit weißem Pelletofen"></div>
    <div class="pellet__dark"></div>
    <div class="pellet__content">
      <h2><span class="title-thin">Die</span><br><span class="title-bold">Pelletöfen</span></h2>
      <p class="lead">Die Wartung beinhaltet:</p>
      <ul class="service-list">
        <li>Reinigung von Sichtscheibe, Brenntopf, Topfhalter, Zwischenboden, gesamter Feuerraum, sämtliche Rauchgaszüge und Aschebehälter</li>
        <li>Reinigung des Saugzuggebläses</li>
        <li>Überprüfung und Reinigung des Luftmengensensors</li>
        <li>Überprüfung der elektrischen Zündung</li>
        <li>Überprüfung der Dichtungen (Türdichtung, Türglasdichtung, Putzdeckeldichtungen)</li>
        <li>Überprüfung der Temperaturwächter</li>
        <li>Probelauf des Gerätes</li>
      </ul>
    </div>
    <div class="price-box">
      <strong>Preise:</strong><br>
      <span class="price--contract">Mit Wartungsvertrag: 140 € inkl. MwSt</span><br>
      Ohne Wartungsvertrag: 180 € inkl. MwSt
    </div>
  </section>

  <section class="panel panel--wood">
    <div class="wood__content">
      <h2>
        <span class="title-thin">Scheitholzöfen,<br>Heizkassetten,<br>Brennzellen,</span><br>
        <span class="title-bold">Holz- und<br>Küchenherde</span>
      </h2>
      <p class="lead">Die Wartung beinhaltet:</p>
      <ul class="service-list">
        <li>Reinigung Schamott Verkleidung, Sichtscheibe, Zwischenboden, gesamter Feuerraum, sämtliche Rauchgaszüge, Aschebehälter</li>
        <li>Reinigung der Abgasrohre (bis 2 m gestreckte Länge)</li>
        <li>Überprüfung der Dichtungen (Türdichtung, Türglas-dichtung, Putzdeckeldichtungen)</li>
        <li>Probelauf des Gerätes</li>
      </ul>
    </div>
    <div class="wood__photo" role="img" aria-label="Fotocollage: Kaminöfen, Heizkassette und Küchenherd mit Feuer"></div>
    <div class="price-block">
      <strong>Preise:</strong><br>
      <span class="price--contract">Mit Wartungsvertrag: 80 € inkl. MwSt</span><br>
      Ohne Wartungsvertrag: 110 € inkl. MwSt
    </div>
  </section>

  <section class="panel panel--tile">
    <div class="tile__photo" role="img" aria-label="Foto: weißer Kachelofen in einem Holzhaus-Wohnraum"></div>
    <svg class="tile__band" viewBox="0 0 370 70" aria-hidden="true">
      <polygon points="0,40 370,0 370,18 0,70" fill="var(--orange)"/>
      <polygon points="0,70 370,18 370,70" fill="#ffffff"/>
    </svg>
    <div class="tile__content">
      <h2><span class="title-thin">Grund-/</span><br><span class="title-bold">Kachelöfen</span></h2>
      <ul class="dot-list">
        <li>Reinigung Schamott Verkleidung, Sichtscheibe, Zwischenboden, gesamter Feuerraum, sämtliche Rauchgaszüge, Aschebehälter</li>
        <li>Reinigung der Abgasrohre (bis zu 2 m gestreckte Länge)</li>
        <li>Überprüfung der Dichtungen (Türdichtung, Türglasdichtung, Putzdeckeldichtungen)</li>
        <li>Probelauf des Gerätes</li>
      </ul>
      <p class="price-group">
        <strong>Preise Kachelofen mit bis zu 4 Öffnungen</strong><br>
        <span class="price--contract">Mit Wartungsvertrag: 350 € inkl. MwSt</span><br>
        Ohne Wartungsvertrag: 390 € inkl. MwSt
      </p>
      <p class="price-group">
        <strong>Preise Kachelofen mit nachgeschalteter Heizfläche</strong><br>
        <span class="price--contract">Mit Wartungsvertrag: 250 € inkl. MwSt</span><br>
        Ohne Wartungsvertrag: 290 € inkl. MwSt
      </p>
    </div>
  </section>

</main>
</body>
</html>
```